"The Plumeworks" nails, eyelash extensions and hair extensions. Need an eye catching design for bu

Need an eye catching design focusing on eyelash extensions, nail extensions and hair extensions. I like the colour green, black, glitter, pink?! need the design to be innovative and 'POP'. I'd like more emphasis on lashes and nails.
I'd like the business name and my phone number on the front of card.
Would really like something different and unique.
"The Plumeworks"
Nails, Eyelash & Hair Extensions
Mira
0417265903

Target Market(s)

20-40

Industry/Entity Type

Beauty Salon

Contact Information for Business Card

Id like my business name, My name and phone number on the front of card
"The Plumeworks".
Mira.
0417265903.
Id like some catchy design involving long lashes with possibly glitter, long hair and nails. Id like the lashes to be the first thing you see at first glance. I'm open to your creative flair. Just need the business card design to 'POP'! I like the colours green, black, pink, silver or gold glitter. wether it's pop art, 3d drawn pictures, isolated pics of lash, nails or hair, card design could be in black and white with isolated colours added..i'm open to your creative flair. use a font which stands out and easy to read.
(The back of the card will be used for writing appointment times.)

Font styles to use
Serif

Colors
6b449b
e667a6
25b39d

Requirements
Must have
• Long lashes, hair, nails.
• one sided
Nice to have
• bright catchy colours, innovative, uniqueness

```html
<!DOCTYPE html>
<html lang="en">
<head>
<meta charset="utf-8">
<title>The Plumeworks – Business Card</title>
<link rel="stylesheet" href="https://fonts.googleapis.com/css2?family=Marcellus&display=swap">
<style>
  :root {
    --page-bg: #e4e3ea;
    --violet-deep: #4a2270;
    --violet: #6b449b;
    --violet-light: #9a6fc4;
    --pink: #d2357a;
    --pink-soft: #e667a6;
    --teal: #25b39d;
    --ring: #ffffff;
    --text-light: #f6eef8;
    --photo-lips: #8a4f86;
    --photo-face: #7a5a8e;
    --photo-hand: #8a2f6e;
  }
  * { margin: 0; padding: 0; box-sizing: border-box; }
  html, body {
    width: 1200px;
    height: 900px;
    overflow: hidden;
    background: var(--page-bg);
  }
  .canvas {
    position: relative;
    width: 1200px;
    height: 900px;
    display: flex;
    align-items: center;
    justify-content: center;
  }
  .business-card {
    position: relative;
    width: 1050px;
    height: 600px;
    overflow: hidden;
    border-radius: 4px;
    background:
      linear-gradient(90deg, rgba(255,255,255,0) 52%, rgba(255,255,255,0.18) 60%, rgba(255,255,255,0) 70%),
      linear-gradient(90deg, var(--violet-deep) 0%, var(--violet) 45%, var(--violet-light) 58%, var(--pink) 100%);
    box-shadow: 0 10px 30px rgba(60, 40, 80, 0.18);
  }
  .card-art {
    position: absolute;
    inset: 0;
    width: 100%;
    height: 100%;
  }
  .brand {
    position: absolute;
    top: 60px;
    right: 80px;
    text-align: right;
    color: var(--text-light);
    font-family: "Marcellus", serif;
  }
  .brand-name {
    font-size: 50px;
    font-weight: 400;
    line-height: 1;
    letter-spacing: 0.5px;
  }
  .brand-tagline {
    margin-top: 4px;
    font-size: 20px;
    line-height: 1.1;
    letter-spacing: 0.3px;
  }
  .contact {
    position: absolute;
    top: 172px;
    right: 40px;
    display: flex;
    align-items: center;
    gap: 12px;
    font-family: "Marcellus", serif;
    color: var(--text-light);
  }
  .contact-text {
    text-align: right;
    font-size: 20px;
    line-height: 1.2;
  }
  .contact-name { display: block; }
  .contact-phone { display: block; letter-spacing: 0.5px; }
  .phone-icon {
    width: 40px;
    height: 40px;
    margin-top: -28px;
  }
</style>
</head>
<body>
<main class="canvas">
  <article class="business-card">
    <svg class="card-art" viewBox="0 0 1050 600" xmlns="http://www.w3.org/2000/svg">
      <defs>
        <linearGradient id="lipsTone" x1="0" y1="0" x2="1" y2="1">
          <stop offset="0" stop-color="#b08aa8"/>
          <stop offset="0.6" stop-color="#8a4f86"/>
          <stop offset="1" stop-color="#5c2c62"/>
        </linearGradient>
        <radialGradient id="faceTone" cx="0.55" cy="0.5" r="0.6">
          <stop offset="0" stop-color="#b89ac4"/>
          <stop offset="0.7" stop-color="#7a5a8e"/>
          <stop offset="1" stop-color="#4a2a5e"/>
        </radialGradient>
        <linearGradient id="handTone" x1="0" y1="0" x2="1" y2="1">
          <stop offset="0" stop-color="#6e2358"/>
          <stop offset="0.5" stop-color="#a05a8e"/>
          <stop offset="1" stop-color="#6a2a60"/>
        </linearGradient>
      </defs>

      <rect class="photo-lips" x="0" y="0" width="440" height="600" fill="url(#lipsTone)"
            role="img" aria-label="Close-up photo of glossy purple lips"/>
      <circle class="ring-top" cx="150" cy="-70" r="175" fill="none" stroke="var(--ring)" stroke-width="22"/>

      <circle class="photo-face" cx="350" cy="245" r="160" fill="url(#faceTone)"
              role="img" aria-label="Photo of a model with long eyelash extensions"/>
      <circle class="ring-face" cx="350" cy="245" r="160" fill="none" stroke="var(--ring)" stroke-width="22"/>

      <circle class="photo-hand" cx="290" cy="690" r="320" fill="url(#handTone)"
              role="img" aria-label="Photo of a hand with long nail extensions"/>
      <circle class="ring-hand" cx="290" cy="690" r="320" fill="none" stroke="var(--ring)" stroke-width="22"/>
    </svg>

    <header class="brand">
      <h1 class="brand-name">The Plumeworks</h1>
      <p class="brand-tagline">Nails, Eyelash &amp; Hair Extensions</p>
    </header>

    <div class="contact">
      <p class="contact-text">
        <span class="contact-name">Mira</span>
        <span class="contact-phone">0417265903</span>
      </p>
      <svg class="phone-icon" viewBox="0 0 40 40" xmlns="http://www.w3.org/2000/svg" aria-hidden="true">
        <circle cx="20" cy="20" r="19" fill="var(--teal)" stroke="#ffffff" stroke-width="2"/>
        <rect x="14" y="10" width="12" height="20" rx="2" fill="none" stroke="#ffffff" stroke-width="2"/>
        <line x1="18" y1="26" x2="22" y2="26" stroke="#ffffff" stroke-width="1.6"/>
      </svg>
    </div>
  </article>
</main>
</body>
</html>
```